New counselling and hypnotherapy business

I'd like a flyer which is relevant to people who want support and to improve their wellbeing which follows the same theme as my website: http://wrenlowtherapy.sitepailo.com
And emphasise that whatever the area of concern, development or growth and I can tailor my knowledge and skills to help.

I'd like to use the same logo and my emphasis is to draw the audience in...therapy and counselling is for people who are "stuck" and having a difficult time...it can also be useful has a personal development tool.

Hypnotherapy

```html
<!DOCTYPE html>
<html lang="en">
<head>
<meta charset="utf-8">
<title>Wrenlow Counselling &amp; Hypnotherapy – Flyer</title>
<link rel="stylesheet" href="https://fonts.googleapis.com/css2?family=Arimo:wght@400;700&display=swap">
<style>
  :root {
    --cream: #fdfbe6;
    --plum: #7a3b72;
    --body-text: #555555;
    --band-pink: #f4b9dd;
    --band-pale: #fbe0ef;
    --photo-violet: #8f77d6;
    --photo-blue: #b9a9ea;
    --sunset-magenta: #c23fa9;
    --sunset-gold: #f7d27a;
  }
  html, body { margin: 0; padding: 0; overflow: hidden; }
  body { background: #e9e6dc; }
  .flyer {
    position: relative;
    width: 1200px;
    height: 857px;
    background: var(--cream);
    overflow: hidden;
    font-family: "Arimo", Arial, sans-serif;
  }
  .artwork { position: absolute; inset: 0; }
  .copy {
    position: absolute;
    left: 518px;
    top: 30px;
    width: 652px;
  }
  .headline {
    margin: 0 0 12px;
    font-size: 25px;
    font-weight: 700;
    color: var(--plum);
    letter-spacing: -0.2px;
  }
  .copy p {
    margin: 0 0 20px;
    font-size: 13.8px;
    line-height: 20px;
    color: var(--body-text);
  }
  .brand {
    position: absolute;
    left: 760px;
    top: 560px;
    width: 330px;
    text-align: center;
    display: flex;
    flex-direction: column;
    align-items: center;
    gap: 14px;
  }
  .brand-dot {
    width: 22px;
    height: 22px;
    border-radius: 50%;
    background: var(--plum);
  }
  .brand-name {
    font-size: 32px;
    line-height: 38px;
    font-weight: 400;
    color: var(--plum);
    margin: 0;
  }
  .contact {
    position: absolute;
    left: 720px;
    top: 754px;
    width: 480px;
    text-align: center;
    font-size: 15.4px;
    line-height: 20px;
    color: #333;
  }
  .contact p { margin: 0; }
  .contact .web { font-weight: 700; color: var(--plum); }
</style>
</head>
<body>
<div class="flyer">
  <svg class="artwork" width="1200" height="857" viewBox="0 0 1200 857">
    <defs>
      <linearGradient id="portraitTone" x1="0" y1="0" x2="1" y2="1">
        <stop offset="0" stop-color="var(--photo-blue)"/>
        <stop offset="0.5" stop-color="var(--photo-violet)"/>
        <stop offset="1" stop-color="#c9a6e4"/>
      </linearGradient>
      <linearGradient id="sunsetTone" x1="0" y1="0" x2="0.3" y2="1">
        <stop offset="0" stop-color="#d866c4"/>
        <stop offset="0.45" stop-color="var(--sunset-magenta)"/>
        <stop offset="0.72" stop-color="var(--sunset-gold)"/>
        <stop offset="1" stop-color="#b23a9c"/>
      </linearGradient>
    </defs>
    <path class="curve-band" d="M575,0 Q440,110 338,205 C410,440 510,670 680,857 L640,857 C490,660 395,430 330,205 Z" fill="var(--band-pale)"/>
    <path class="curve-band" d="M560,0 Q430,105 330,198 C400,430 500,660 662,857 L640,857 C480,660 385,430 318,205 Z" fill="var(--band-pink)"/>
    <path class="photo-portrait" role="img" aria-label="Photo of a thoughtful man resting his head in his hand, comforted by a woman, in violet tones" d="M0,0 L530,0 L0,588 Z" fill="url(#portraitTone)"/>
    <path class="photo-beach" role="img" aria-label="Photo of children playing on a beach at sunset in magenta and gold tones" d="M0,588 L330,208 C395,435 495,662 640,857 L0,857 Z" fill="url(#sunsetTone)"/>
    <path class="edge-band" d="M0,588 L330,208 L342,218 L0,606 Z" fill="var(--band-pink)"/>
  </svg>

  <section class="copy">
    <h1 class="headline">Trusted. Professional. An approach tailored to you</h1>
    <p>There are times in all of our lives when we feel we have lost our way, we need a listening ear or we simply want somebody to work together with to help us reach the next step in our journey, whatever that may be. Maybe that sounds like you and you're looking for somebody to help you take that first step or maybe you simply want somebody to share your concerns with and really feel heard.</p>
    <p>I am a fully qualified counsellor and I'm able to provide a safe, confidential environment for you to speak, to feel, to be heard and valued as an individual in what can be a scary and challenging world.</p>
    <p>I have experience of working with people with a wide range of concerns. Some examples include loss and grief, depression, anxiety, relationships, self-esteem, eating disorders, confidence, general personal development and growth. I find this work really rewarding and it's been a privilege to work with all of these people.</p>
    <p>In addition to a more typical counselling role, I am able to offer hypnotherapy. I find this works really well in combination with counselling. I am also happy to offer this on its own for specific things such as giving up smoking, phobias, relaxation, confidence and much more.</p>
    <p>I'm happy to support individuals over fourteen years of age and couples on a face-to-face basis for short, medium or long term therapy.</p>
  </section>

  <div class="brand">
    <span class="brand-dot"></span>
    <p class="brand-name">Wrenlow<br>Counselling &amp;<br>Hypnotherapy</p>
  </div>

  <address class="contact" style="font-style:normal">
    <p>Address: Wrenlow Counselling &amp; Hypnotherapy,</p>
    <p>12B, Mill Lane, Eastbrook West Sussex BN4 2QT</p>
    <p>Tel. 07700 900418 &bull; Email.wrenlowtherapy@mailbox.com</p>
    <p class="web">www.wrenlowtherapy.sitepailo.com</p>
  </address>
</div>
</body>
</html>
```